Halvet Energy Letter Head- with all subsidiaries

We need a letterhead that will showcase all Halvet Energy subsidiaries, while still have Halvet Energy logo ontop.

```html
<!DOCTYPE html>
<html lang="en">
<head>
<meta charset="utf-8">
<title>Halvet Energy Letterhead</title>
<link href="https://fonts.googleapis.com/css2?family=Open+Sans:wght@400;600;700&display=swap" rel="stylesheet">
<style>
  :root {
    --gold: #c6a55c;
    --charcoal: #3d3d3d;
    --ink: #4a4a4a;
    --paper: #ffffff;
    --blue: #1aa3e0;
  }
  * { margin: 0; padding: 0; box-sizing: border-box; }
  html, body { width: 1040px; height: 1200px; overflow: hidden; background: var(--paper); }
  body { font-family: "Open Sans", Arial, sans-serif; color: var(--ink); }
  .letterhead { position: relative; width: 1040px; height: 1200px; background: var(--paper); }

  .brand { position: absolute; top: 70px; left: 0; width: 100%; display: flex; justify-content: center; align-items: center; gap: 14px; }
  .brand-mark { width: 34px; height: 34px; background: var(--gold); }
  .brand-name { font-size: 40px; font-weight: 700; color: var(--charcoal); letter-spacing: 1px; }

  .letter { position: absolute; top: 212px; left: 97px; width: 840px; font-size: 15px; }
  .issue-date { margin-bottom: 20px; }
  .recipient { line-height: 18px; margin-bottom: 50px; }
  .salutation { margin-bottom: 32px; }
  .letter-body p { line-height: 27px; text-align: justify; margin-bottom: 27px; }
  .closing { margin-top: 52px; }
  .signatory { margin-top: 58px; }
  .signatory-name { font-size: 19px; font-weight: 600; color: var(--charcoal); }
  .signatory-role { margin-top: 4px; }

  .footer-band { position: absolute; left: 0; bottom: 0; width: 1040px; height: 112px; }
  .contact { position: absolute; left: 100px; top: 1122px; color: #fff; font-size: 14px; line-height: 19px; list-style: none; }
  .contact li { display: flex; align-items: center; gap: 6px; }
  .contact svg { width: 11px; height: 11px; fill: var(--gold); }

  .subsidiaries { position: absolute; inset: 0; pointer-events: none; }
  .sub { position: absolute; display: flex; align-items: center; gap: 6px; font-size: 12px; font-weight: 700; color: var(--charcoal); white-space: nowrap; }
  .sub-mark { width: 12px; height: 12px; background: var(--gold); flex: none; }
  .sub-mark.round { border-radius: 50%; background: var(--blue); }
</style>
</head>
<body>
<main class="letterhead">
  <header class="brand">
    <span class="brand-mark"></span>
    <span class="brand-name">Halvet Energy</span>
  </header>

  <section class="letter">
    <p class="issue-date">Issuing Date: May 5, 2018</p>
    <p class="recipient">Name Of Employee Mr. XYZABC<br>Address of Employee<br>Address Line 2 etc..</p>
    <p class="salutation">Dear Mr.XYZABC</p>
    <div class="letter-body">
      <p>Lorem Ipsum has been the industry's standard dummy text ever since the 1500s, when an unknown printer took a galley of type and scrambled it to make a type specimen book. It has survived not only five centuries, but also the leap into electronic typesetting, remaining essentially unchanged. It was popularised in the 1960s with the release of Letraset sheets containing Lorem Ipsum passages, and more recently with desktop publishing software like Aldus PageMaker including versions of Lorem Ipsum.</p>
      <p>Lorem Ipsum is simply dummy text of the printing and typesetting industry. Lorem Ipsum has been the industry's standard dummy text ever since the 1500s, when an unknown printer took a galley of type and scrambled it to make a type specimen book.</p>
      <p>It has survived not only five centuries, but also the leap into electronic typesetting, remaining essentially unchanged. It was popularised in the 1960s with the release of Letraset sheets containing Lorem IpsumIpsum passages.</p>
    </div>
    <p class="closing">Yours Sincerely</p>
    <div class="signatory">
      <p class="signatory-name">Daniel Morrow</p>
      <p class="signatory-role">Managing Director</p>
    </div>
  </section>

  <svg class="footer-band" viewBox="0 0 1040 112" preserveAspectRatio="none">
    <polygon points="0,3 290,3 415,67 1040,67 1040,112 0,112" fill="var(--charcoal)"/>
    <polyline points="0,2 290,2 412,66" fill="none" stroke="var(--gold)" stroke-width="4"/>
  </svg>

  <ul class="contact">
    <li><svg viewBox="0 0 10 10"><path d="M2 1h2l1 2-1 1a5 5 0 0 0 2 2l1-1 2 1v2c-4 0-7-3-7-7z"/></svg>044-555 010 200</li>
    <li><svg viewBox="0 0 10 10"><path d="M0 2h10v6H0zM0 2l5 3 5-3" /></svg>info@halvetenergy.com</li>
    <li><svg viewBox="0 0 10 10"><circle cx="5" cy="5" r="5"/></svg>www.halvetenergy.com</li>
  </ul>

  <div class="subsidiaries">
    <div class="sub" style="left:382px; top:1112px;"><span class="sub-mark"></span>Fivepoint Electric</div>
    <div class="sub" style="left:520px; top:1112px;"><span class="sub-mark round"></span>Brightline Electrical</div>
    <div class="sub" style="left:672px; top:1046px;"><span class="sub-mark"></span>Halvet Logistics</div>
    <div class="sub" style="left:820px; top:1046px;"><span class="sub-mark"></span>Halvet Aviation</div>
    <div class="sub" style="left:672px; top:1104px;"><span class="sub-mark"></span>Halvet Caribbean</div>
    <div class="sub" style="left:820px; top:1104px;"><span class="sub-mark"></span>Halvet Acquisitions</div>
  </div>
</main>
</body>
</html>
```